Lumora business card for a plastic surgeon

we need a business card for plastic surgeons that work on a clinic called LUMORA.
we want a clean design and the following informations: name of the doctor, doctor's registration number (called CRM), telephone, address, facebook, instagram.
Colors: white, blue tones, light brown/ coffee

facebook and instagram: lumoracirurgiaestetica

Industry/Entity Type

Business

Contact Information for Business Card

clean design

Font styles to use
Serif
Sans Serif
Other font styles liked:
• helvetica light

Colors
cee9f5
85cae6
85abd2
3276b5
cfeae6
cedeed
eaf1f7

Requirements
Must have
• doctor's name
• identification number (called CRM)
• contact (phone, facebook, instagram, address)

```html
<!DOCTYPE html>
<html lang="pt">
<head>
<meta charset="utf-8">
<title>Lumora – business card</title>
<link rel="stylesheet" href="https://fonts.googleapis.com/css2?family=Cinzel:wght@400&family=Open+Sans:wght@400;600;700&display=swap">
<style>
  :root {
    --stage: #5f5e5f;
    --navy: #033358;
    --navy-soft: #0a4670;
    --cyan: #00c0de;
    --ice: #d0e8f5;
    --ice-faint: #e9f6fb;
    --ink: #0c3a5e;
    --text-dark: #333333;
    --white: #ffffff;
  }
  * { margin: 0; padding: 0; box-sizing: border-box; }
  html, body { width: 1018px; height: 1200px; overflow: hidden; }
  body {
    background: var(--stage);
    position: relative;
    font-family: "Open Sans", Arial, sans-serif;
  }
  .card { position: absolute; overflow: hidden; }
  .card--front { left: 47px; top: 52px; width: 926px; height: 529px; background: var(--navy); }
  .card--back { left: 41px; top: 621px; width: 926px; height: 528px; background: var(--white); }

  .motif { position: absolute; border-radius: 50%; }
  .card--front .motif {
    left: 10px; top: -40px; width: 470px; height: 470px;
    background: radial-gradient(circle, var(--navy-soft) 0%, rgba(10,70,112,0.35) 55%, rgba(3,51,88,0) 72%);
  }
  .card--back .motif {
    left: 10px; top: -20px; width: 470px; height: 470px;
    background: radial-gradient(circle, var(--ice-faint) 0%, rgba(233,246,251,0.5) 55%, rgba(255,255,255,0) 72%);
  }

  .brand { position: absolute; text-align: center; font-family: "Cinzel", "Times New Roman", serif; }
  .brand__name { display: block; color: var(--cyan); font-weight: 400; line-height: 1; }
  .brand__field { display: block; line-height: 1; letter-spacing: 1px; }
  .card--front .brand { left: 213px; top: 198px; width: 500px; }
  .card--front .brand__name { font-size: 84px; }
  .card--front .brand__field { font-size: 33px; color: var(--white); margin-top: 24px; }
  .card--back .brand { left: 34px; top: 226px; width: 500px; }
  .card--back .brand__name { font-size: 88px; }
  .card--back .brand__field { font-size: 33px; color: var(--ink); margin-top: 24px; }

  .band { position: absolute; }
  .band svg { position: absolute; inset: 0; }
  .band__text { position: relative; color: var(--white); white-space: nowrap; }
  .band--slogan { left: 211px; top: 466px; width: 715px; height: 63px; }
  .band--slogan .band__text { font-size: 29px; left: 37px; top: 8px; }
  .band--address { left: 0; top: 460px; width: 725px; height: 68px; }
  .band--address .band__text { font-size: 25px; left: 22px; top: 16px; }
  .tab { position: absolute; right: 0; top: 0; width: 432px; height: 34px; }

  .divider { position: absolute; left: 534px; top: 157px; width: 2px; height: 254px; background: var(--cyan); }

  .contact { position: absolute; left: 581px; top: 135px; }
  .contact__name { font-size: 42px; color: var(--ink); line-height: 1.1; font-weight: 400; }
  .contact__name strong { font-weight: 700; }
  .contact__crm { font-size: 24px; color: var(--cyan); margin-top: 2px; }
  .contact__list { list-style: none; margin-top: 12px; }
  .contact__item {
    display: flex; align-items: center; height: 40.5px;
    font-size: 21px; font-weight: 700; color: var(--text-dark);
  }
  .contact__icon {
    width: 20px; height: 20px; margin-right: 6px; border-radius: 4px;
    background: var(--cyan); flex: none;
  }
</style>
</head>
<body>

<section class="card card--front">
  <div class="motif" role="img" aria-label="Faint decorative brand motif"></div>
  <div class="brand">
    <span class="brand__name">LUMORA</span>
    <span class="brand__field">CIRURGIA PLÁSTICA</span>
  </div>
  <div class="band band--slogan">
    <svg width="715" height="63" viewBox="0 0 715 63"><path d="M20 10 Q22 0 34 0 H715 V63 H0 Z" fill="var(--cyan)"/></svg>
    <p class="band__text">Add your slogan here if any or add Dr Name</p>
  </div>
</section>

<section class="card card--back">
  <div class="motif" role="img" aria-label="Faint decorative brand motif"></div>
  <svg class="tab" viewBox="0 0 432 34"><path d="M0 0 H432 V34 H20 Q10 34 7 24 Z" fill="var(--ice)"/></svg>
  <div class="brand">
    <span class="brand__name">LUMORA</span>
    <span class="brand__field">CIRURGIA PLÁSTICA</span>
  </div>
  <div class="divider"></div>
  <div class="contact">
    <h1 class="contact__name"><strong>NAME</strong> HERE</h1>
    <p class="contact__crm">CRM 121212</p>
    <ul class="contact__list">
      <li class="contact__item">
        <svg class="contact__icon" viewBox="0 0 20 20"><rect width="20" height="20" rx="4" fill="var(--cyan)"/><path d="M6 4 L8.5 4 L9.5 7 L8 8.3 Q9.5 11.5 12 12.5 L13.3 11 L16 12 L16 14.5 Q15 16 13 15.6 Q6 13.5 4.5 6.5 Q4.5 4.5 6 4 Z" fill="var(--white)"/></svg>
        000.1234.5678
      </li>
      <li class="contact__item">
        <svg class="contact__icon" viewBox="0 0 20 20"><rect width="20" height="20" rx="4" fill="var(--cyan)"/><rect x="6.5" y="3.5" width="7" height="13" rx="1.5" fill="none" stroke="var(--white)" stroke-width="1.6"/><circle cx="10" cy="14" r="0.9" fill="var(--white)"/></svg>
        000.1234.2564
      </li>
      <li class="contact__item"><span class="contact__icon"></span>lumoracirurgiaestetica</li>
      <li class="contact__item"><span class="contact__icon"></span>lumoracirurgiaestetica</li>
      <li class="contact__item">
        <svg class="contact__icon" viewBox="0 0 20 20"><rect width="20" height="20" rx="4" fill="var(--cyan)"/><rect x="3.5" y="5.5" width="13" height="9" fill="var(--white)"/><path d="M3.5 5.5 L10 10.5 L16.5 5.5" fill="none" stroke="var(--cyan)" stroke-width="1.2"/></svg>
        info@abcd.com
      </li>
    </ul>
  </div>
  <div class="band band--address">
    <svg width="725" height="68" viewBox="0 0 725 68"><path d="M0 0 H693 Q704 0 707 10 L725 68 H0 Z" fill="var(--cyan)"/></svg>
    <p class="band__text">8630 abcdeford Rd. Suite 154 your city, mnopqurs 21046</p>
  </div>
</section>

</body>
</html>
```